New Business Card for Casual Beachfront Cafe

Quirky Beachfront Cafe at Moana, South Australia needs a DOUBLE SIDED business card to print on PrintHarbor.

Target Market(s)

Business Cards sit on the counter for Guests to take with them. Please view our website www.saltreefcafe.com.au to get a feel for the Cafe. You may also view our Instagram at @saltreefcafe

Industry/Entity Type

Cafe / Restaurant

Contact Information for Business Card

Information equivalent to: Breakfast, Lunch, Dinner, Coffee, Takeaway / 117 Parade Kestrel Bay SA 5920 / Menu & Opening Hours: www.saltreefcafe.com.au / ph (08) 8461 9273

Requirements
Must have
• Information equivalent to: Breakfast, Lunch, Dinner, Coffee, Takeaway / 117 Parade Kestrel Bay SA 5920 / Menu & Opening Hours: www.saltreefcafe.com.au / ph (08) 8461 9273
Nice to have
• Potentially some of our trademark colours (Cafe can be searched via Seekly)
Should not have
• Must NOT have image of the building. May have the logo provided on one side but not necessarily, depending on how you wish to design the card

```html
<!DOCTYPE html>
<html lang="en">
<head>
<meta charset="utf-8">
<title>Salt Reef Cafe – Business Card</title>
<link rel="stylesheet" href="https://fonts.googleapis.com/css2?family=Montserrat:wght@400;500;700;800&display=swap">
<style>
  :root {
    --page: #2b2b2d;
    --card-blue: #1b447f;
    --card-edge: #16396b;
    --sun-yellow: #f6e500;
    --rust-orange: #c9581f;
    --ink-white: #ffffff;
  }
  * { box-sizing: border-box; margin: 0; padding: 0; }
  html, body {
    width: 1200px; height: 960px; overflow: hidden;
    background: var(--page);
    font-family: "Montserrat", Arial, sans-serif;
    color: var(--ink-white);
  }
  .sheet {
    position: relative; width: 1200px; height: 960px;
    display: flex; flex-direction: column; align-items: center; justify-content: center; gap: 44px;
  }
  .card {
    position: relative; width: 720px; height: 412px;
    background: var(--card-blue);
    border-radius: 26px;
    box-shadow: 0 4px 0 var(--card-edge), 0 8px 0 var(--card-edge), 0 14px 28px rgba(0,0,0,.45);
    overflow: hidden;
  }

  /* Hours side */
  .card-hours .brand-name {
    position: absolute; left: 48px; top: 132px; width: 280px;
    font-weight: 800; font-size: 54px; line-height: 1.02; letter-spacing: 1px;
    color: var(--sun-yellow); text-transform: uppercase;
  }
  .divider-lines { position: absolute; left: 330px; top: 70px; }
  .hours {
    position: absolute; left: 420px; top: 64px; width: 290px;
  }
  .hours-title {
    font-weight: 800; font-size: 17px; letter-spacing: .3px; margin-bottom: 12px;
    text-transform: uppercase;
  }
  .hours-title .accent-yellow { color: var(--sun-yellow); }
  .hours-title .accent-orange { color: var(--rust-orange); }
  .hours-list { list-style: none; font-size: 17px; font-weight: 500; line-height: 1.72; }
  .hours-list .day { display: inline-block; width: 50px; }
  .hours-note { margin-top: 14px; font-size: 15.5px; font-weight: 500; line-height: 1.5; }

  /* Contact side */
  .card-contact { text-align: center; }
  .card-contact .brand-name {
    position: absolute; left: 0; right: 0; top: 70px;
    font-weight: 800; font-size: 60px; line-height: 1.02; letter-spacing: 1px;
    color: var(--sun-yellow); text-transform: uppercase;
  }
  .contact-lines {
    position: absolute; left: 0; right: 0; top: 236px;
    font-size: 18px; font-weight: 500; line-height: 1.75;
  }
  .contact-row { display: flex; align-items: center; justify-content: center; gap: 8px; }
  .contact-row .gap { width: 10px; }
  .icon { width: 18px; height: 18px; flex: none; }
</style>
</head>
<body>
<main class="sheet">

  <section class="card card-hours" aria-label="Card side with kitchen hours">
    <div class="brand-name">Salt Reef<br>Cafe</div>
    <svg class="divider-lines" width="70" height="270" viewBox="0 0 70 270" aria-hidden="true">
      <line x1="8" y1="0" x2="52" y2="270" stroke="var(--sun-yellow)" stroke-width="1.6"/>
      <line x1="22" y1="20" x2="62" y2="250" stroke="var(--sun-yellow)" stroke-width="1.6"/>
      <line x1="0" y1="40" x2="36" y2="240" stroke="var(--sun-yellow)" stroke-width="1.6"/>
    </svg>
    <div class="hours">
      <h2 class="hours-title"><span class="accent-yellow">Winter</span> <span class="accent-orange">Kitchen</span> <span class="accent-yellow">Hours</span></h2>
      <ul class="hours-list">
        <li><span class="day">Mon</span>Closed</li>
        <li><span class="day">Tues</span>Closed</li>
        <li><span class="day">Wed</span>8am-2pm, 5pm-9pm</li>
        <li><span class="day">Thur</span>8am-2pm, 5pm-9pm</li>
        <li><span class="day">Fri</span>8am-2pm, 5pm-9pm</li>
        <li><span class="day">Sat</span>7:30am-9pm</li>
        <li><span class="day">Sun</span>7:30am-7pm</li>
      </ul>
      <p class="hours-note">Closing time may vary slightly.<br>Guests may stay later.</p>
    </div>
  </section>

  <section class="card card-contact" aria-label="Card side with contact details">
    <div class="brand-name">Salt Reef<br>Cafe</div>
    <div class="contact-lines">
      <p>Breakfast, Lunch, Dinner, Coffee</p>
      <p>Takeaway / 117 Parade Kestrel Bay SA 5920 / Menu &amp;</p>
      <p class="contact-row">
        <svg class="icon" viewBox="0 0 24 24" aria-hidden="true"><path fill="var(--ink-white)" d="M6.6 10.8a15 15 0 0 0 6.6 6.6l2.2-2.2c.3-.3.7-.4 1-.2 1.1.4 2.3.6 3.6.6.6 0 1 .4 1 1V20c0 .6-.4 1-1 1A17 17 0 0 1 3 4c0-.6.4-1 1-1h3.5c.6 0 1 .4 1 1 0 1.3.2 2.5.6 3.6.1.3 0 .7-.2 1z"/></svg>
        <span>(08) 8461 9273</span><span class="gap"></span>
        <svg class="icon" viewBox="0 0 24 24" aria-hidden="true"><circle cx="12" cy="12" r="9" fill="none" stroke="var(--ink-white)" stroke-width="2"/><path d="M3 12h18M12 3c3 3 3 15 0 18M12 3c-3 3-3 15 0 18" fill="none" stroke="var(--ink-white)" stroke-width="1.5"/></svg>
        <span>www.saltreefcafe.com.au</span><span class="gap"></span>
        <svg class="icon" viewBox="0 0 24 24" aria-hidden="true"><circle cx="12" cy="12" r="8" fill="none" stroke="var(--ink-white)" stroke-width="2"/></svg>
        <span>@saltreefcafe</span>
      </p>
    </div>
  </section>

</main>
</body>
</html>
```